To design a brand identity that is simple and creative with 'Valtor' as the brand name, I like modern simple fonts like helvetica neue, I want to print both sides of the card, I am open to dark front and white back, but the design needs to transfer well to letter heads and email signatures, I am looking for sophisticated and elegant, but open minded about clever and off the wall, I do not do 'boring' Valtor Holdings is the mother company for a small group, specialising in Management & consulting, Software development and construction, we have a high level of integrity, we are transparent and accountable for what we do. my images are provided as a guide only, Im not expecting them to be just copied, Im looking for a creator and passionate thinker, who will put life into their work.

Target Market(s)

usually business minded people who are looking for something different in me, such as leadership, confidence and focus with thinking that is per haps a little outside the box..

Industry/Entity Type

Construction

Requirements
Must have
• clean, minmalistic
Nice to have
• custom logo
Should not have
• boring, traditional

```html
<!DOCTYPE html>
<html lang="en">
<head>
<meta charset="utf-8">
<title>Valtor Holdings — Business Card</title>
<link rel="stylesheet" href="https://fonts.googleapis.com/css2?family=Quicksand:wght@300;400;500;700&display=swap">
<style>
  :root {
    --backdrop: #e9e6e1;
    --card-dark: #2e2d2d;
    --card-dark-edge: #3a3939;
    --accent-orange: #e2693b;
    --accent-orange-soft: #d8764e;
    --cream: #e6dcc6;
    --muted-orange: #c8754f;
  }
  * { box-sizing: border-box; margin: 0; padding: 0; }
  html, body {
    width: 1200px;
    height: 762px;
    overflow: hidden;
    background: var(--backdrop);
  }
  .sheet {
    width: 1200px;
    height: 762px;
    display: flex;
    align-items: center;
    justify-content: center;
    gap: 40px;
  }
  .card {
    position: relative;
    width: 540px;
    height: 309px;
    border-radius: 3px;
    background: linear-gradient(135deg, var(--card-dark) 0%, var(--card-dark-edge) 100%);
    box-shadow: 0 10px 24px rgba(0,0,0,0.18);
    overflow: hidden;
    font-family: "Quicksand", "Helvetica Neue", sans-serif;
  }

  /* Shared wordmark: name set in the card's text font, one weight, one colour */
  .wordmark {
    display: flex;
    align-items: center;
  }
  .wordmark .mark-square {
    background: var(--accent-orange);
    flex: none;
  }
  .wordmark .brand-name {
    font-weight: 500;
    text-transform: uppercase;
    color: var(--accent-orange);
    line-height: 1;
  }
  .motto {
    font-weight: 400;
    color: var(--cream);
    white-space: nowrap;
  }

  /* Back side */
  .card-back .identity {
    position: absolute;
    left: 44px;
    top: 110px;
    width: 156px;
  }
  .card-back .wordmark { gap: 10px; }
  .card-back .mark-square { width: 18px; height: 18px; }
  .card-back .brand-name {
    font-size: 24px;
    letter-spacing: 5px;
  }
  .card-back .motto {
    margin-top: 8px;
    padding-left: 28px;
    font-size: 10px;
    letter-spacing: 0.4px;
  }
  .divider {
    position: absolute;
    left: 214px;
    top: 36px;
    width: 1.5px;
    height: 120px;
    background: var(--accent-orange);
  }
  .contact {
    position: absolute;
    left: 236px;
    top: 40px;
    color: var(--muted-orange);
    font-size: 13px;
    line-height: 1.9;
    font-weight: 400;
  }
  .contact .email {
    font-weight: 700;
    font-size: 16px;
    color: var(--accent-orange);
    line-height: 1.4;
  }
  .services {
    position: absolute;
    left: 44px;
    bottom: 42px;
    font-weight: 300;
    font-size: 26px;
    color: var(--accent-orange-soft);
    letter-spacing: 0.5px;
  }

  /* Front side */
  .card-front .identity {
    position: absolute;
    left: 50px;
    top: 104px;
  }
  .card-front .wordmark { gap: 26px; }
  .card-front .mark-square { width: 58px; height: 58px; }
  .card-front .brand-name {
    font-size: 66px;
    letter-spacing: 14px;
  }
  .card-front .motto {
    margin-top: 22px;
    padding-left: 86px;
    font-size: 17px;
    letter-spacing: 2px;
  }
</style>
</head>
<body>
  <main class="sheet">
    <section class="card card-back" aria-label="Card back">
      <div class="identity">
        <div class="wordmark">
          <span class="mark-square"></span>
          <span class="brand-name">Valtor</span>
        </div>
        <div class="motto">Built with purpose.</div>
      </div>
      <div class="divider"></div>
      <div class="contact">
        <div class="email">dana@valtor.holdings</div>
        <div class="role">Client Ambassador</div>
        <div class="phone">+61 049 512 304</div>
        <div class="address">Po Box 514 Northvale 6100</div>
      </div>
      <div class="services">Management. software. construction</div>
    </section>

    <section class="card card-front" aria-label="Card front">
      <div class="identity">
        <div class="wordmark">
          <span class="mark-square"></span>
          <span class="brand-name">Valtor</span>
        </div>
        <div class="motto">Built with purpose.</div>
      </div>
    </section>
  </main>
</body>
</html>
```